Looking to design a new sign for our church.

Looking for a new sign
4 x 8 feet dimension
We are renaming the church "Keller Ridge Community Church"
looking for legible graphics
Would like some type of backdrop being a family tree (oak) / open to other ideas as you are led
I have included a pic of the old sign for your review
would like to incorporate our ministry logo on the lower right hand corner of the sign / see file attached

```html
<!DOCTYPE html>
<html lang="en">
<head>
<meta charset="UTF-8">
<title>Keller Ridge Community Church – Sign</title>
<link href="https://fonts.googleapis.com/css2?family=Bebas+Neue&display=swap" rel="stylesheet">
<style>
  :root {
    --leaf-light: #c9ec7a;
    --leaf-mid: #7fcb35;
    --leaf-deep: #3f8f1f;
    --bark: #4a3d2c;
    --sky: #f4fbe6;
    --title-fill: rgba(250, 250, 248, 0.93);
    --title-stroke: #3b302b;
    --panel: rgba(255, 255, 255, 0.62);
    --schedule-blue: #175a98;
  }
  * { margin: 0; padding: 0; box-sizing: border-box; }
  html, body { width: 1200px; height: 600px; overflow: hidden; }
  body { font-family: "Bebas Neue", "Arial Narrow", sans-serif; }

  .sign {
    position: relative;
    width: 1200px;
    height: 600px;
    overflow: hidden;
  }
  .canopy-backdrop {
    position: absolute;
    inset: 0;
    background:
      radial-gradient(ellipse at 22% 35%, var(--sky) 0%, rgba(244,251,230,0) 28%),
      radial-gradient(ellipse at 60% 85%, rgba(244,251,230,0.8) 0%, rgba(244,251,230,0) 30%),
      linear-gradient(105deg, rgba(74,61,44,0) 70%, rgba(74,61,44,0.75) 88%, rgba(74,61,44,0.55) 100%),
      linear-gradient(160deg, var(--leaf-light) 0%, var(--leaf-mid) 45%, var(--leaf-deep) 100%);
  }

  .church-name {
    position: absolute;
    left: 0;
    right: 0;
    top: 122px;
    text-align: center;
    font-weight: 400;
    color: var(--title-fill);
    -webkit-text-stroke: 5px var(--title-stroke);
    paint-order: stroke fill;
    line-height: 0.86;
    padding-left: 30px;
  }
  .church-name__primary {
    display: block;
    font-size: 196px;
    letter-spacing: 4px;
  }
  .church-name__secondary {
    display: block;
    font-size: 120px;
    letter-spacing: 3px;
    margin-top: 10px;
  }

  .schedule-panel {
    position: absolute;
    left: 102px;
    top: 453px;
    width: 1024px;
    height: 147px;
    background: var(--panel);
  }
  .schedule {
    position: absolute;
    left: 70px;
    top: 63px;
    display: flex;
    align-items: center;
    gap: 13px;
    color: var(--schedule-blue);
    font-size: 28px;
    line-height: 1;
    letter-spacing: 0.3px;
    white-space: nowrap;
  }

  .ministry-mark {
    position: absolute;
    right: 20px;
    top: 25px;
    width: 62px;
    display: flex;
    flex-direction: column;
    align-items: center;
    gap: 6px;
    color: var(--schedule-blue);
    font-size: 13px;
    line-height: 1.05;
    text-align: center;
  }
  .ministry-mark svg { display: block; }
</style>
</head>
<body>
  <main class="sign">
    <div class="canopy-backdrop" role="img" aria-label="Photo looking up into a green oak tree canopy with sunlit leaves and a thick bark trunk on the right"></div>

    <h1 class="church-name">
      <span class="church-name__primary">Keller Ridge</span>
      <span class="church-name__secondary">Community Church</span>
    </h1>

    <section class="schedule-panel">
      <p class="schedule">
        <span class="schedule__item">10:30AM Worship Service</span>
        <span class="schedule__divider">|</span>
        <span class="schedule__item">9:30AM Sunday School</span>
        <span class="schedule__divider">|</span>
        <span class="schedule__item">6:00PM Wednesday Service</span>
      </p>
      <div class="ministry-mark">
        <svg width="30" height="30" viewBox="0 0 30 30" aria-hidden="true">
          <circle cx="15" cy="15" r="13" fill="none" stroke="#175a98" stroke-width="2"/>
        </svg>
        <span>Ridge Light<br>Ministries</span>
      </div>
    </section>
  </main>
</body>
</html>
```